The Gentle Moonlit Harbour Journey

This book accompanies a video workshop. The book explains who our guardian angels are, what is their purpose, how to connect with them for wisdom & guidance. How to manifest what we world like bring into our lives by asking the Angels. The book contains meditation exercises, lots of information and fun facts about how our angels give us messages and guidance and how to become more intuitive. How to use angel oracle cards to receive guidance from our angels.
I'm quite an upbeat, happy person, so the book is written very warmly and is a collection of all the information that out ther, drawn together neatly by me, with my own unique take on all things angelic. Along with personal stories and anecdotes about how and why I became interested in angels and what they have taught me. It's fun, fresh, lighthearted and modern. Not at all serious, just extremely uplifting and positive, so I would really like the cover to reflect this.

Target Market(s)

Anyone who is interested in angels. From my chatterloop page activity I find it is mostly women of all ages who are interested in angels

Font styles to use
Serif
Sans Serif
Script

Colors
ea8dbb
f04a50
e667a6
e34197
85abd2
886aae
b7a5cd
6b449b
fbee3e

Requirements
Must have
• A more feminine appeal
• Look quite modern & upbeat but also calming and open
• I would like it to look etherel in some way. I definitely dont want something that looks like a cartoon or clip art
Should not have
• No dark colours or sinister imagery. I don't want people to feel like thus can't do the & it's only special people who can connect with their angels
• No haunting imagery!

```html
<!DOCTYPE html>
<html lang="en">
<head>
<meta charset="utf-8">
<title>Angels – Cover Options</title>
<link rel="stylesheet" href="https://fonts.googleapis.com/css2?family=Federo&family=Arimo:wght@700&display=swap">
<style>
  :root {
    --page: #ffffff;
    --frame: #c9c9c9;
    --ink: #6b449b;
    --ink-soft: #7a4aa8;
    --lilac: #e4a2e6;
    --lilac-light: #f3d2f4;
    --petal: #fbe6fb;
    --sky: #cdeefc;
    --sky-fade: #eef9fe;
  }
  * { box-sizing: border-box; margin: 0; padding: 0; }
  html, body {
    width: 1200px;
    height: 771px;
    overflow: hidden;
    background: var(--page);
  }
  .sheet {
    position: relative;
    width: 1200px;
    height: 771px;
  }
  .cover {
    position: absolute;
    top: 42px;
    width: 456px;
    height: 676px;
    border: 1px solid var(--frame);
    overflow: hidden;
    background: var(--page);
  }
  .cover--plain { left: 56px; }
  .cover--sky { left: 675px; }

  .sky-panel {
    position: absolute;
    top: 0;
    right: 0;
    width: 334px;
    height: 337px;
    background: linear-gradient(200deg, var(--sky) 0%, var(--sky-fade) 70%, rgba(255,255,255,0) 100%);
  }

  .wing-art {
    position: absolute;
    inset: 0;
    background:
      radial-gradient(ellipse 70% 45% at 0% 100%, var(--lilac) 0%, var(--lilac) 45%, rgba(228,162,230,0) 100%),
      radial-gradient(ellipse 90% 60% at 60% 75%, var(--lilac-light) 0%, rgba(243,210,244,0.6) 45%, rgba(251,230,251,0) 100%),
      linear-gradient(35deg, var(--petal) 0%, rgba(251,230,251,0.5) 50%, rgba(255,255,255,0) 80%);
  }
  .cover--sky .wing-art {
    background:
      radial-gradient(ellipse 70% 45% at 0% 100%, var(--lilac) 0%, var(--lilac) 45%, rgba(228,162,230,0) 100%),
      radial-gradient(ellipse 90% 60% at 60% 75%, var(--lilac-light) 0%, rgba(243,210,244,0.6) 45%, rgba(251,230,251,0) 100%);
  }

  .cover__author {
    position: absolute;
    top: 60px;
    right: 50px;
    font-family: "Arimo", Arial, sans-serif;
    font-weight: 700;
    font-size: 23px;
    color: var(--ink-soft);
    letter-spacing: 0.2px;
  }
  .cover__title {
    position: absolute;
    top: 92px;
    right: 46px;
    font-family: "Federo", Georgia, serif;
    font-size: 96px;
    line-height: 1;
    color: var(--ink);
    letter-spacing: -1px;
  }
  .cover__tagline {
    position: absolute;
    right: 50px;
    bottom: 42px;
    font-family: "Arimo", Arial, sans-serif;
    font-weight: 700;
    font-size: 14.5px;
    line-height: 19px;
    text-align: right;
    color: var(--ink-soft);
  }
</style>
</head>
<body>
  <main class="sheet">
    <section class="cover cover--plain">
      <div class="wing-art" role="img" aria-label="Large feathered angel wing illustration in soft lilac and white sweeping across the cover"></div>
      <p class="cover__author">Rosalind Avery</p>
      <h1 class="cover__title">Angels</h1>
      <p class="cover__tagline">Connect with your angels<br>bring love, healing and divine guidance<br>to every area of your life</p>
    </section>

    <section class="cover cover--sky">
      <div class="sky-panel"></div>
      <div class="wing-art" role="img" aria-label="Large feathered angel wing illustration in soft lilac and white sweeping across the cover"></div>
      <p class="cover__author">Rosalind Avery</p>
      <h1 class="cover__title">Angels</h1>
      <p class="cover__tagline">Connect with your angels<br>bring love, healing and divine guidance<br>to every area of your life</p>
    </section>
  </main>
</body>
</html>
```